A 24' X 36" SIGN TO ANNOUNCE "ORDER YOUR TURKEY EARLY"

MUST INCLUDE OUR LOGO(PROVIDED), black background, TEXT to include
all natural
farm raised
no hormones

The sign needs to be designed for vertical(portrait) viewing. The logo needs to be smaller and emphasis on TURKEY

Farm

```html
<!DOCTYPE html>
<html lang="en">
<head>
<meta charset="utf-8">
<title>Order Your Turkey Early — Halverson Market</title>
<link rel="stylesheet" href="https://fonts.googleapis.com/css2?family=Bebas+Neue&family=Short+Stack&display=swap">
<style>
  :root {
    --ink: #000000;
    --accent: #ffec00;
  }
  html, body {
    margin: 0;
    padding: 0;
    background: var(--ink);
    overflow: hidden;
  }
  .sign {
    position: relative;
    width: 801px;
    height: 1200px;
    background: var(--ink);
    color: var(--accent);
    overflow: hidden;
  }
  .sign-frame {
    position: absolute;
    left: 30px;
    top: 29px;
    width: 735px;
    height: 1138px;
    border: 3px solid var(--accent);
  }
  .headline {
    position: absolute;
    left: 0;
    width: 100%;
    margin: 0;
    text-align: center;
    font-family: "Bebas Neue", "Oswald", sans-serif;
    font-weight: 400;
    line-height: 1;
    white-space: nowrap;
  }
  .headline-order { top: 107px; font-size: 147px; letter-spacing: 1px; }
  .headline-turkey { top: 241px; font-size: 295px; letter-spacing: 2px; }
  .headline-early { top: 514px; font-size: 147px; letter-spacing: 1px; }

  .brand-row {
    position: absolute;
    left: 60px;
    top: 755px;
    width: 681px;
    height: 40px;
    display: flex;
    align-items: center;
    justify-content: space-between;
  }
  .brand-rule {
    width: 92px;
    height: 3px;
    background: var(--accent);
  }
  .brand-name {
    font-family: "Bebas Neue", "Oswald", sans-serif;
    font-size: 46px;
    line-height: 1;
    letter-spacing: 3px;
    color: var(--accent);
  }

  .features {
    position: absolute;
    left: 203px;
    top: 884px;
    margin: 0;
    padding: 0;
    list-style: none;
  }
  .feature {
    display: flex;
    align-items: center;
    height: 58px;
    margin-bottom: 31px;
  }
  .feature-icon {
    width: 58px;
    height: 58px;
    flex: none;
  }
  .feature-label {
    margin-left: 31px;
    font-family: "Short Stack", "Comic Neue", cursive;
    font-size: 40px;
    line-height: 1;
    letter-spacing: 2px;
    color: var(--accent);
  }
</style>
</head>
<body>
<main class="sign">
  <div class="sign-frame"></div>

  <h1 class="headline headline-order">ORDER YOUR</h1>
  <p class="headline headline-turkey">TURKEY</p>
  <p class="headline headline-early">EARLY</p>

  <div class="brand-row">
    <span class="brand-rule"></span>
    <span class="brand-name">HALVERSON MARKET</span>
    <span class="brand-rule"></span>
  </div>

  <ul class="features">
    <li class="feature">
      <svg class="feature-icon" viewBox="0 0 58 58" aria-hidden="true">
        <circle cx="29" cy="29" r="29" fill="var(--accent)"/>
        <path d="M30 12 C18 22 18 36 27 44 C38 36 40 22 30 12 Z" fill="var(--ink)"/>
        <path d="M29 18 C26 28 26 38 27 47" stroke="var(--accent)" stroke-width="2" fill="none"/>
      </svg>
      <span class="feature-label">All natural</span>
    </li>
    <li class="feature">
      <svg class="feature-icon" viewBox="0 0 58 58" aria-hidden="true">
        <circle cx="29" cy="29" r="29" fill="var(--accent)"/>
        <path d="M13 46 V26 L20 16 H38 L45 26 V46 Z" fill="var(--ink)"/>
        <rect x="24" y="22" width="10" height="5" fill="var(--accent)"/>
        <rect x="21" y="31" width="16" height="15" fill="var(--accent)"/>
        <path d="M23 33 L35 44 M35 33 L23 44" stroke="var(--ink)" stroke-width="2"/>
      </svg>
      <span class="feature-label">Farm raised</span>
    </li>
    <li class="feature">
      <svg class="feature-icon" viewBox="0 0 58 58" aria-hidden="true">
        <circle cx="29" cy="29" r="29" fill="var(--accent)"/>
        <circle cx="29" cy="29" r="20" fill="none" stroke="var(--ink)" stroke-width="3"/>
        <path d="M15 15 L43 43" stroke="var(--ink)" stroke-width="3"/>
        <path d="M20 38 L36 22 M33 19 L39 25 M17 41 L21 37" stroke="var(--ink)" stroke-width="3" fill="none"/>
      </svg>
      <span class="feature-label">No hormones</span>
    </li>
  </ul>
</main>
</body>
</html>
```